Aesthetics Company Flyer (description of services)

We need a 5.5"x8.5" flyer describing the services we offer at velvet horizon aesthetics. We are an aesthetics company located in Conroe TX. Our products and services can be found at www.vhaesthetics-demo.com/services . We would like to see designs that are cohesive with our brand and website: https://www.vhaesthetics-demo.com/

```html
<!DOCTYPE html>
<html lang="en">
<head>
<meta charset="utf-8">
<title>Velvet Horizon Aesthetics – Services Flyer</title>
<link rel="stylesheet" href="https://fonts.googleapis.com/css2?family=Montserrat:wght@400;500;600;700;800&family=Oswald:wght@300;400&family=Roboto+Condensed:wght@400&display=swap">
<style>
  :root {
    --frame-pink: #f6c8d6;
    --panel-peach: #f3d5cf;
    --panel-rose: #efc6c8;
    --ink-dark: #2b2a2d;
    --blush: #f7c6d3;
    --ring-rose: #d9a6b7;
    --logo-rose: #c98aa0;
    --swoosh-pink: #de8fae;
    --box-pink: rgba(238, 172, 186, 0.38);
    --text-dark: #2a2426;
    --white: #ffffff;
  }
  * { margin: 0; padding: 0; box-sizing: border-box; }
  html, body { width: 850px; height: 1200px; overflow: hidden; background: #ffffff; }
  .flyer {
    position: relative;
    width: 850px;
    height: 1200px;
    font-family: "Montserrat", sans-serif;
    color: var(--text-dark);
    overflow: hidden;
  }
  .flyer-art { position: absolute; inset: 0; }

  .brand {
    position: absolute;
    left: 560px; top: 150px;
    display: flex; align-items: center; gap: 10px;
  }
  .brand-dot {
    width: 22px; height: 22px; border-radius: 50%;
    background: var(--logo-rose);
    flex: none;
  }
  .brand-name {
    font-family: "Montserrat", sans-serif;
    font-weight: 500;
    font-size: 15px;
    letter-spacing: 2.5px;
    line-height: 1.35;
    color: var(--logo-rose);
    text-transform: uppercase;
  }

  .tagline {
    position: absolute;
    right: 70px; top: 274px;
    text-align: right;
    font-family: "Oswald", sans-serif;
    font-weight: 400;
    color: var(--blush);
    font-size: 44px;
    line-height: 39px;
    letter-spacing: -0.5px;
    text-transform: uppercase;
  }
  .tagline .minor { font-size: 29px; font-weight: 300; }

  .services-title {
    position: absolute;
    left: 62px; top: 636px;
    font-weight: 700;
    font-size: 33px;
    letter-spacing: 0.5px;
    color: var(--text-dark);
    padding-bottom: 4px;
    border-bottom: 1px solid rgba(42, 36, 38, 0.35);
  }

  .service { position: absolute; }
  .service-name {
    font-weight: 500;
    font-size: 16px;
    letter-spacing: 0.3px;
    text-transform: uppercase;
    color: var(--text-dark);
    margin-bottom: 10px;
  }
  .service-name small { font-size: 9px; letter-spacing: 0; }
  .service-sub {
    display: block;
    text-transform: none;
    font-size: 12px;
    font-weight: 400;
    margin-top: 1px;
  }
  .service-copy {
    background: var(--box-pink);
    border-radius: 3px;
    padding: 8px 8px 10px 12px;
    font-size: 11px;
    line-height: 14.4px;
    color: var(--text-dark);
  }

  .svc-weightloss  { left: 169px; top: 0; }
  .contact {
    position: absolute;
    right: 73px; top: 1055px;
    text-align: right;
    color: var(--white);
  }
  .contact-phone { font-weight: 800; font-size: 43px; line-height: 48px; letter-spacing: 0.5px; }
  .contact-email { font-weight: 700; font-size: 19px; line-height: 26px; }
  .contact-address {
    font-family: "Roboto Condensed", sans-serif;
    font-size: 20px; line-height: 30px;
  }
</style>
</head>
<body>
<main class="flyer">
  <svg class="flyer-art" width="850" height="1200" viewBox="0 0 850 1200" aria-hidden="false">
    <defs>
      <linearGradient id="panelTone" x1="0" y1="0" x2="0" y2="1">
        <stop offset="0" stop-color="#f4d8d0"/>
        <stop offset="1" stop-color="#efc5c8"/>
      </linearGradient>
      <linearGradient id="heroTone" x1="0" y1="0" x2="1" y2="0.3">
        <stop offset="0" stop-color="#d9a77d"/>
        <stop offset="0.3" stop-color="#c79463"/>
        <stop offset="0.6" stop-color="#e8c2aa"/>
        <stop offset="0.85" stop-color="#6b4a3a"/>
        <stop offset="1" stop-color="#2b2a2d"/>
      </linearGradient>
      <linearGradient id="logoPanel" x1="0" y1="0" x2="1" y2="1">
        <stop offset="0" stop-color="#fde9ee"/>
        <stop offset="1" stop-color="#fbe0e8"/>
      </linearGradient>
      <linearGradient id="photoInject" x1="0" y1="0" x2="1" y2="1">
        <stop offset="0" stop-color="#f3f1f2"/>
        <stop offset="0.5" stop-color="#e9c9b6"/>
        <stop offset="1" stop-color="#f7f5f6"/>
      </linearGradient>
      <linearGradient id="photoPeel" x1="0" y1="0" x2="1" y2="1">
        <stop offset="0" stop-color="#9a9697"/>
        <stop offset="0.45" stop-color="#e8c53a"/>
        <stop offset="1" stop-color="#3a3838"/>
      </linearGradient>
      <linearGradient id="photoNeuro" x1="0" y1="0" x2="1" y2="1">
        <stop offset="0" stop-color="#eceaea"/>
        <stop offset="0.5" stop-color="#b5826a"/>
        <stop offset="1" stop-color="#f2f0f1"/>
      </linearGradient>
      <clipPath id="clipInject"><circle cx="183" cy="518" r="104"/></clipPath>
      <clipPath id="clipPeel"><circle cx="445" cy="552" r="123"/></clipPath>
      <clipPath id="clipNeuro"><circle cx="695" cy="580" r="100"/></clipPath>
    </defs>

    <!-- frame -->
    <rect class="frame" x="0" y="0" width="850" height="1200" fill="var(--frame-pink)"/>
    <rect class="panel" x="18" y="21" width="814" height="1166" fill="url(#panelTone)"/>

    <!-- hero band -->
    <path class="hero-dark" d="M18 21 H832 V478 C640 448 400 470 18 652 Z" fill="var(--ink-dark)"/>
    <path class="hero-photo" role="img" aria-label="Portrait photo of two smiling women with glowing skin"
          d="M18 21 H520 C560 140 560 300 540 470 C380 500 200 560 18 652 Z" fill="url(#heroTone)"/>
    <path class="hero-swoosh" d="M18 652 C400 470 640 448 832 478 V500 C640 470 420 490 18 668 Z" fill="#e7b2c2"/>

    <!-- logo panel -->
    <path class="logo-panel" d="M458 21 H832 V268 C700 272 545 210 458 21 Z" fill="url(#logoPanel)"/>
    <path class="logo-edge" d="M458 21 C545 210 700 272 832 268 V280 C690 284 535 220 452 21 Z" fill="var(--ring-rose)"/>

    <!-- service photos -->
    <circle cx="183" cy="518" r="111" fill="var(--ring-rose)"/>
    <rect role="img" aria-label="Photo of a filler injection treatment on a client's cheek" x="70" y="405" width="230" height="230" fill="url(#photoInject)" clip-path="url(#clipInject)"/>
    <circle cx="445" cy="552" r="130" fill="var(--ring-rose)"/>
    <rect role="img" aria-label="Photo of a yellow chemical peel being brushed onto a client's face" x="315" y="420" width="260" height="260" fill="url(#photoPeel)" clip-path="url(#clipPeel)"/>
    <circle cx="695" cy="580" r="107" fill="var(--ring-rose)"/>
    <rect role="img" aria-label="Photo of a neurotoxin injection treatment" x="590" y="475" width="210" height="210" fill="url(#photoNeuro)" clip-path="url(#clipNeuro)"/>

    <!-- footer -->
    <path class="footer-swoosh" d="M18 1187 V1172 C210 1108 430 1058 640 1036 C440 1074 280 1132 200 1187 Z" fill="var(--swoosh-pink)"/>
    <path class="footer-dark" d="M200 1187 C300 1112 540 1040 832 1034 V1187 Z" fill="var(--ink-dark)"/>
  </svg>

  <div class="brand">
    <span class="brand-dot"></span>
    <span class="brand-name">Velvet Horizon<br>Aesthetics</span>
  </div>

  <h1 class="tagline">
    <span class="minor">We</span> Change<br>
    The World<br>
    <span class="minor">One</span> Beautiful<br>
    Face <span class="minor">at a time</span>
  </h1>

  <h2 class="services-title">OUR SERVICES</h2>

  <section class="service" style="left:54px; top:705px; width:240px;">
    <h3 class="service-name" style="margin-left:10px;">Weightloss</h3>
    <p class="service-copy">Semaglutide stimulates insulin to be released from the pancreas in an effort to slow down gastric emptying and inhibits inappropriate release of sugars after we eat. Simply put, this process ultimately reduces our food intake from within, thereby leading to weight loss.</p>
  </section>

  <section class="service" style="left:315px; top:697px; width:240px;">
    <h3 class="service-name" style="margin-left:10px; margin-bottom:6px;">Neurotoxin<span class="service-sub">(Wrinkle Relaxer)</span></h3>
    <p class="service-copy">Neurotoxin injections lessens facial lines that can give you a tired appearance. These lines are produced by repeated muscle contractions most noticeable on the forehead, between the eyebrows and around the eyes. Smoothlyn® relaxes these muscles to give the skin a smooth appearance.<br>(Smoothlyn®, Relaxia®, Calmera®)</p>
  </section>

  <section class="service" style="left:572px; top:698px; width:232px;">
    <h3 class="service-name" style="margin-left:10px;">Dermal Fillers</h3>
    <p class="service-copy">Fibrin Growth Factor (FGF) facial treatment enhances skin rejuvenation, scar and wound rejuvenation, and hair restoration by injecting plasma rich fibrin into the face. This component of contains fibrin growth factors and proteins that enhance cellular healing, rejuvenate tone, and promote new collagen growth.</p>
  </section>

  <section class="service" style="left:64px; top:889px; width:230px;">
    <h3 class="service-name" style="margin-left:-6px;">Fibrin Growth Factor <small>(FGF)</small></h3>
    <p class="service-copy">Dermal filler treatments plump up smile and frown lines, thin lips, and decrease cheek wrinkles and chin folds with FDA-approved volumizing hyaluronic acid, thus allow skin to restore fullness from the inside out.<br>LIPS<br>SMILE LINES/NASOLABIAL FOLDS</p>
  </section>

  <section class="service" style="left:323px; top:889px; width:232px;">
    <h3 class="service-name" style="margin-left:4px;">DermaGlide®</h3>
    <p class="service-copy">DermaGlide® is a microneedling treatment that generates the skin’s self-repair mechanism and activates collagen and elastin production. Microneedling is great for scarring, problems with texture, enlarged pores, and even stretch marks.</p>
  </section>

  <section class="service" style="left:572px; top:889px; width:225px;">
    <h3 class="service-name" style="margin-left:0;">Chemical Peels</h3>
    <p class="service-copy">Chemical Peels improve skin texture correcting pigmentation concerns, sun damage, and scarring.</p>
  </section>

  <address class="contact" style="font-style:normal;">
    <div class="contact-phone">555 014 2287</div>
    <div class="contact-email">hello@vhaesthetics-demo.com</div>
    <div class="contact-address">1200 Example Pkwy #150, Conroe, TX 77000</div>
  </address>
</main>
</body>
</html>
```